2-Sided A4 Brochure

We're looking for a double-sided A4 brochure for print and PDF. Company is in online travel and is called "Pebble Lantern". This brochure is intended for partner organisations looking to license our technology for use on their websites. As such, the design should maintain the inspirational feel of typical travel designs whilst also conveying a good deal of professionalism.
A selection of images we've taken from the technology has be supplied along with logo and copy. Please utilise at least a few of these images in any and all designs.
Preferred colours are #56A0CD and #00286B. Copy includes headings and contact details should be in a breakout box.
Finished size: 210mm x 297mm
Bleed size (2mm): 214mm x 301mm
Safe size (5mm): 204mm x 291mm
Industry/Entity Type
Travel
Look and feel
Each slider illustrates characteristics of the customer's brand and the style your logo design should communicate.

```html
<!DOCTYPE html>
<html lang="en">
<head>
<meta charset="UTF-8">
<title>Pebble Lantern – Partner Brochure</title>
<link href="https://fonts.googleapis.com/css2?family=Nunito+Sans:wght@400;600;700&display=swap" rel="stylesheet">
<style>
  :root {
    --backdrop: #ffffff;
    --navy: #1f2f66;
    --navy-deep: #00286b;
    --brand-blue: #56a0cd;
    --front-sky: #b6c2e7;
    --body-ink: #1d2b5e;
    --logo-teal: #1f9b9b;
    --photo-fill: #3bb0d6;
    --back-text: #dbeaf6;
    --white: #ffffff;
  }
  * { box-sizing: border-box; margin: 0; padding: 0; }
  html, body {
    width: 1200px; height: 800px; overflow: hidden;
    background: var(--backdrop);
    font-family: "Nunito Sans", Arial, sans-serif;
  }
  .spread {
    position: relative; width: 1200px; height: 800px;
    display: flex; justify-content: center; align-items: center; gap: 60px;
  }
  .page {
    width: 509px; height: 720px; position: relative; overflow: hidden;
    display: flex; flex-direction: column;
  }

  /* Front page */
  .page--front { background: var(--front-sky); }
  .heading-band {
    background: var(--navy); color: var(--white);
    font-weight: 600; font-size: 19px; text-align: center;
    padding: 7px 16px;
  }
  .page--front .heading-band { margin-top: 40px; }
  .intro {
    color: var(--body-ink); font-size: 12.6px; line-height: 1.42;
    padding: 12px 26px 0;
  }
  .brand-mark {
    display: flex; flex-direction: column; align-items: center;
    margin-top: 30px;
  }
  .brand-mark__name {
    display: flex; align-items: center; gap: 10px;
    color: var(--logo-teal); font-size: 42px; font-weight: 600;
  }
  .brand-mark__dot {
    width: 14px; height: 14px; border-radius: 50%; background: var(--logo-teal);
  }
  .brand-mark__tagline {
    align-self: flex-end; margin-right: 70px;
    color: var(--body-ink); font-size: 13px;
  }
  .hero-photo {
    flex: 1; margin-top: 18px;
    background: var(--photo-fill);
  }

  /* Back page */
  .page--back { background: var(--brand-blue); padding-top: 44px; }
  .page--back .heading-band { text-align: left; padding-left: 30px; }
  .section-copy {
    color: var(--back-text); font-size: 10.6px; line-height: 1.42;
    padding: 10px 24px 16px 30px;
  }
  .social-box {
    margin-top: auto; background: var(--navy); color: var(--white);
  }
  .social-box .heading-band { background: transparent; }
  .social-box__body { padding: 6px 30px 18px; }
  .social-box__copy { color: var(--back-text); font-size: 10.6px; line-height: 1.42; }
  .social-box__brand {
    display: flex; justify-content: flex-end; align-items: center; gap: 6px;
    color: var(--brand-blue); font-size: 15px; font-weight: 600; margin-top: 8px;
  }
  .social-box__brand-dot { width: 7px; height: 7px; border-radius: 50%; background: var(--brand-blue); }
  .contact__label { font-size: 11px; margin-top: 10px; }
  .contact__line { font-size: 14px; line-height: 1.3; }
</style>
</head>
<body>
<main class="spread">
  <section class="page page--front">
    <h1 class="heading-band">Pebble Lantern for Tourism Organizations</h1>
    <p class="intro">Pebble Lantern offers travelers the most powerful and convenient way to plan and book their next fantastic getaway. Selecting from flights, hotels, tours, cruises, restaurants, activities and more, travelers can create custom itineraries complete with a personalized, full-color brochure before sharing them with friends or submitting them anonymously for quotes from hundreds of travel agents. Pebble Lantern's industry-leading, patent-pending technology mirrors the experience of visiting the local, high-street travel agency whilst affording the privacy, convenience and power of transacting online.</p>
    <div class="brand-mark">
      <div class="brand-mark__name"><span>PebbleLantern.com</span><span class="brand-mark__dot"></span></div>
      <div class="brand-mark__tagline">Where great journeys begin.</div>
    </div>
    <div class="hero-photo" role="img" aria-label="Photo of windswept trees on a white chalk cliff above a turquoise sea"></div>
  </section>

  <section class="page page--back">
    <h2 class="heading-band">Not Just a Planner – Not Just a Booking</h2>
    <p class="section-copy">Travel planners simply plan while booking engines simply book – Pebble Lantern bridges this gap by combining the convenience of the internet with the trust and protection of registered travel agents. With no affiliation to content providers, Pebble Lantern is free to promote the content best suited to your users. And when the user has compiled their ideal itinerary from our vast range of tailored product, they can send their itinerary to hundreds of travel agents for a free, anonymous quote. Pebble Lantern charges no membership fees to users meaning our service is offered completely free of charge to travelers. Instead, travel agents subscribe to receive and quote on the itineraries submitted via the site. This means that our goal and your goal are the same: getting people to your destination.</p>

    <h2 class="heading-band">Our Technology, Your Brand</h2>
    <p class="section-copy">We are passionate about our reputation as trusted and unbiased providers of travel advice. Our brand is important to us; just as yours is to you. Many holiday planners are light on features offering only basic search functionality on your site before clicking through to theirs. With just a few lines of HTML, Pebble Lantern is completely integrated into your site allowing users to build an entire itinerary never leaving your page. Without ever clicking-through, clicking-out or popping-up, users can search for content, view high-resolution images, consult detailed maps, create their itinerary and print or share their customized brochure with friends. This means you can leverage the industry-leading technology of Pebble Lantern all the while protecting your brand asset.</p>

    <div class="social-box">
      <h2 class="heading-band">Travel is Social</h2>
      <div class="social-box__body">
        <p class="social-box__copy">Travelers love to share their experiences and what better way than by the power of social media. Pebble Lantern not only offers complete web integration with leading social media such as Chatterbox, Chirper and Circlenet but is also available as a fully-branded Chatterbox app and mobile app. You can offer your users the power and convenience of Pebble Lantern via the channel of their choice with all interactions linked back directly to your social media presence. Leverage the virality and interactivity of social media with Pebble Lantern's seamless integration into your own social media assets.</p>
        <div class="social-box__brand"><span>PebbleLantern.com</span><span class="social-box__brand-dot"></span></div>
        <p class="contact__label">Contact Details :</p>
        <p class="contact__line">www.pebblelantern.com</p>
        <p class="contact__line">partners@pebblelantern.com</p>
      </div>
    </div>
  </section>
</main>
</body>
</html>
```